Brisk & Summit a function beverage brand

Looking to have our FB page designed/configured/setup to optimize D2C sales and communications.

Target Market(s)

US Consumers, that are interested in functional beverages, hemp, hemp derivatives, wellbeing, energy drinks, above the age of 21.

Industry/Entity Type

Functional Food and Beverages

Requirements
Must have
• full D2C sales, marketing and communications.

```html
<!DOCTYPE html>
<html lang="en">
<head>
<meta charset="utf-8">
<title>Brisk &amp; Summit — Page Cover</title>
<link href="https://fonts.googleapis.com/css2?family=Exo+2:wght@600;700&family=Quicksand:wght@600;700&display=swap" rel="stylesheet">
<style>
  :root {
    --stage: #eceef1;
    --ink-dark: #121a20;
    --ink-deep: #1f2e38;
    --bean-mid: #2b2f30;
    --mint: #12e59a;
    --white: #ffffff;
  }
  * { margin: 0; padding: 0; box-sizing: border-box; }
  html, body {
    width: 1200px; height: 800px; overflow: hidden;
    background: var(--stage);
  }
  .canvas {
    position: relative; width: 1200px; height: 800px;
  }
  .cover {
    position: absolute; left: 50px; top: 70px;
    width: 1100px; height: 419px; overflow: hidden;
    color: var(--white); text-align: center;
  }
  .cover-photo {
    position: absolute; inset: 0;
    background:
      radial-gradient(ellipse at 22% 30%, #3a3c3b 0%, transparent 45%),
      radial-gradient(ellipse at 85% 80%, #343635 0%, transparent 45%),
      radial-gradient(ellipse at 50% 45%, #0d1418 0%, var(--ink-dark) 70%);
  }
  .cover-content {
    position: relative; z-index: 1;
    padding-top: 56px;
  }
  .brand-lockup {
    display: inline-flex; align-items: center; gap: 12px;
  }
  .brand-dot {
    width: 46px; height: 46px; border-radius: 50%;
    border: 2px solid var(--white);
  }
  .brand-name {
    font-family: "Exo 2", sans-serif; font-weight: 700;
    font-size: 34px; color: var(--mint); letter-spacing: 0.5px;
  }
  .headline {
    margin-top: 36px;
    font-family: "Exo 2", sans-serif; font-weight: 700;
    font-size: 52px; line-height: 56px; letter-spacing: 0.5px;
  }
  .accent-bar {
    width: 78px; height: 9px; margin: 20px auto 0;
    background: var(--mint);
  }
  .subline {
    margin: 22px auto 0; width: 540px;
    font-family: "Quicksand", sans-serif; font-weight: 700;
    font-size: 23px; line-height: 28px;
  }
  .profile-badge {
    position: absolute; left: 50px; top: 520px;
    width: 234px; height: 234px; border-radius: 50%;
    background: var(--ink-deep);
    display: flex; align-items: center; justify-content: center;
  }
  .profile-name {
    font-family: "Exo 2", sans-serif; font-weight: 700;
    font-size: 30px; line-height: 34px; color: var(--mint);
    text-align: center;
  }
</style>
</head>
<body>
<main class="canvas">
  <section class="cover">
    <div class="cover-photo" role="img" aria-label="Dark close-up photograph of roasted coffee beans"></div>
    <div class="cover-content">
      <div class="brand-lockup">
        <span class="brand-dot"></span>
        <span class="brand-name">Brisk &amp; Summit</span>
      </div>
      <h1 class="headline">Functional Cannabis Beverages<br>for Active Lifestyles</h1>
      <div class="accent-bar"></div>
      <p class="subline">Mirco-Dosed Cannabis, Nootropics, Adaptogens &amp; Energy Boosters</p>
    </div>
  </section>
  <div class="profile-badge">
    <span class="profile-name">Brisk &amp;<br>Summit</span>
  </div>
</main>
</body>
</html>
```